Criação de Papelaria Profissional para Construção & Engenharia
" Empresa que atua em incorporação imobiliária, administrando a construção de edifícios "

```html
<!DOCTYPE html>
<html lang="pt-BR">
<head>
<meta charset="utf-8">
<title>Envelope — Ferraz Rocha Engenharia</title>
<link href="https://fonts.googleapis.com/css2?family=Montserrat:wght@400;600;700&display=swap" rel="stylesheet">
<style>
  :root{
    --board:#e4e4e4;
    --brand-blue:#1f4b8e;
    --brand-blue-dark:#173c75;
    --paper:#ffffff;
    --ink:#5a5f66;
    --muted:#8a8f96;
    --rule:#c9c9c9;
  }
  *{margin:0;padding:0;box-sizing:border-box}
  html,body{width:1200px;height:1200px;overflow:hidden}
  body{background:var(--board);font-family:"Montserrat",sans-serif;position:relative}
  .board-frame{position:absolute;inset:0}
  .board-title{
    position:absolute;top:26px;left:0;width:1200px;text-align:center;
    font-weight:700;font-size:28px;letter-spacing:1px;color:var(--brand-blue-dark)
  }
  .envelope{position:absolute;top:240px;width:472px;height:715px;box-shadow:0 2px 6px rgba(0,0,0,.18)}
  .envelope--front{left:115px;background:var(--brand-blue)}
  .envelope--back{left:612px;background:var(--paper);overflow:hidden}
  .envelope__flap{position:absolute;top:0;left:0;width:100%;height:80px}
  .envelope__stripe{position:absolute;left:0;width:100%}
  .envelope--front .envelope__stripe{bottom:18px;height:6px;background:var(--paper)}
  .envelope--back .envelope__stripe{bottom:0;height:14px;background:var(--brand-blue)}
  .wordmark{position:absolute;display:flex;align-items:center;gap:14px}
  .wordmark__square{width:46px;height:46px;flex:none}
  .wordmark__name{font-weight:600;font-size:24px;letter-spacing:.5px;line-height:1}
  .wordmark__tag{font-weight:400;font-size:10px;letter-spacing:7px;margin-top:7px}
  .envelope--front .wordmark{left:80px;top:335px;color:var(--paper)}
  .envelope--front .wordmark__square{background:var(--paper)}
  .envelope--back .wordmark{left:78px;top:335px;color:var(--ink)}
  .envelope--back .wordmark__square{background:var(--brand-blue)}
  .envelope--back .wordmark__tag{color:var(--muted)}
  .contact-bar{
    position:absolute;left:38px;right:30px;bottom:38px;display:flex;justify-content:space-between;align-items:center;
    font-size:9.5px;color:var(--ink)
  }
  .contact-bar__item{display:flex;align-items:center;gap:5px}
  .contact-bar__item svg{width:12px;height:12px;flex:none}
  .contact-bar__address{line-height:1.35}
  .board-signoff{left:430px;top:1066px;color:var(--ink)}
  .board-signoff .wordmark__name{font-size:27px}
  .board-signoff .wordmark__square{width:52px;height:52px;background:var(--brand-blue)}
  .board-signoff .wordmark__tag{color:var(--muted);font-size:11px}
</style>
</head>
<body>
  <svg class="board-frame" width="1200" height="1200" viewBox="0 0 1200 1200" aria-hidden="true">
    <rect x="68" y="68" width="1064" height="1064" rx="30" fill="none" stroke="var(--rule)" stroke-width="2"/>
    <path d="M400 40 H80 A40 40 0 0 0 40 80 V1120 A40 40 0 0 0 80 1160 H390" fill="none" stroke="var(--brand-blue)" stroke-width="8"/>
    <path d="M800 40 H1120 A40 40 0 0 1 1160 80 V1120 A40 40 0 0 1 1120 1160 H810" fill="none" stroke="var(--brand-blue)" stroke-width="8"/>
  </svg>

  <h1 class="board-title">ENVELOPE</h1>

  <section class="envelope envelope--front">
    <div class="wordmark">
      <span class="wordmark__square"></span>
      <div>
        <div class="wordmark__name">FERRAZ ROCHA</div>
        <div class="wordmark__tag">ENGENHARIA</div>
      </div>
    </div>
    <span class="envelope__stripe"></span>
  </section>

  <section class="envelope envelope--back">
    <svg class="envelope__flap" viewBox="0 0 472 80" preserveAspectRatio="none" aria-hidden="true">
      <path d="M0 0 H472 V20 Q472 62 430 64 H42 Q0 62 0 20 Z" fill="var(--brand-blue)"/>
    </svg>
    <div class="wordmark">
      <span class="wordmark__square"></span>
      <div>
        <div class="wordmark__name">FERRAZ ROCHA</div>
        <div class="wordmark__tag">ENGENHARIA</div>
      </div>
    </div>
    <div class="contact-bar">
      <span class="contact-bar__item">
        <svg viewBox="0 0 12 12"><path d="M3 1 L5 3.5 L4 5 Q5 7 7 8 L8.5 7 L11 9 L10 11 Q5 11 1 3 Z" fill="var(--ink)"/></svg>
        (11) 94020-3150
      </span>
      <span class="contact-bar__item">
        <svg viewBox="0 0 12 12"><rect x="1" y="2.5" width="10" height="7" fill="none" stroke="var(--ink)" stroke-width="1.2"/><path d="M1 2.5 L6 6.5 L11 2.5" fill="none" stroke="var(--ink)" stroke-width="1.2"/></svg>
        contato@ferrazrocha.com.br
      </span>
      <span class="contact-bar__item">
        <svg viewBox="0 0 12 12"><path d="M6 11 Q2 6.5 2 4.5 A4 4 0 0 1 10 4.5 Q10 6.5 6 11 Z" fill="none" stroke="var(--ink)" stroke-width="1.2"/><circle cx="6" cy="4.5" r="1.3" fill="var(--ink)"/></svg>
        <span class="contact-bar__address">R. das Acácias, 120<br>Santos SP</span>
      </span>
    </div>
    <span class="envelope__stripe"></span>
  </section>

  <div class="wordmark board-signoff">
    <span class="wordmark__square"></span>
    <div>
      <div class="wordmark__name">FERRAZ ROCHA</div>
      <div class="wordmark__tag">ENGENHARIA</div>
    </div>
  </div>
</body>
</html>
```